Motivational Quotes Poster Series

This is a 3 poster design series for Ridgeway Haul Academy. The size of each poster should be 18 inches wide and 24 inches tall. The goal of these posters is to serve as motivational "signs" to be hung in the office area for the employees (not customers). These employees are instructors/teachers, teaching students how to drive semi trucks. While each design is a separate poster and design, we're posting as 1 project because we'd like some continuity between the series. Below we'll break down the details of all 3 posters...

Poster #1
Text that must appear on poster - "If You Want The Best Out Of Each Student" and "Give The Best Of You!" Note: While this text must appear on the poster, you can arrange in the layout as you see fit. For example, first line could be at top of poster and second line on bottom.

Poster #2
Text that must appear on poster - "Invest In People" and "Change Someone's Life" (same notes apply as in 1st poster)

Poster #3
Text that must appear on poster - "Today Is..." and "Just Another Day For You" and "The Most Important Day In Their Life" Note: This can be laid out on the poster however you see fit, but each phrase needs to be separate and it needs to flow.

Target Market(s)

Truck Driver Training Instructors - These are middle-aged, mostly male, masculine type personalities.

Industry/Entity Type

Training

Requirements
Must have
• Must have noted text from description
Must have working files (ie - PSD, EPS, AI, etc) provided
Must have common theme between each poster in series
Must have easy to read font and layout
Must have product dimensions of 18 inches (width) by 24 inches (height). If design uses full dimensions please include quarter inch bleed.
Nice to have
• Nice to have a trucking theme...related to trucking industry, but not over the top. Example - This could mean subtle injection of background tire tracks, but by no means are tire tracks required.

For inspiration, you can visit the site at http://www.ridgewayhaulacademy.com. While you can use the colors of the site/logo, you can still branch out between each poster to try new colors within reason.

Note: While we've attached the logo to this project, it COULD be used but doesn't HAVE to be included in the design. The logo IS NOT a focal point. The phrases in the poster ARE the focal point.

```html
<!DOCTYPE html>
<html lang="en">
<head>
<meta charset="utf-8">
<title>Ridgeway Haul Academy – Motivational Poster Series</title>
<link href="https://fonts.googleapis.com/css2?family=Roboto+Condensed:wght@400;700&display=swap" rel="stylesheet">
<style>
  :root {
    --canvas: #ffffff;
    --label-bg: #000000;
    --label-text: #ffffff;
    --shadow: rgba(0, 0, 0, 0.35);
    --road-dark: #2e2e2e;
    --road-mid: #6e6e6e;
    --road-light: #9a9a9a;
    --dusk: #15110d;
    --olive: #6f6a2a;
    --amber: #b9772c;
    --rust: #8a2a14;
    --sky-blue: #2f3fa8;
    --haze: #f2f2f4;
  }
  * { margin: 0; padding: 0; box-sizing: border-box; }
  html, body {
    width: 1200px;
    height: 534px;
    overflow: hidden;
    background: var(--canvas);
  }
  .series {
    position: relative;
    width: 1200px;
    height: 534px;
    font-family: "Roboto Condensed", "Arial Narrow", sans-serif;
  }
  .poster {
    position: absolute;
    top: 34px;
    width: 349px;
    height: 466px;
    overflow: hidden;
    box-shadow: 2px 3px 5px var(--shadow);
  }
  .poster--best { left: 34px; }
  .poster--invest { left: 426px; }
  .poster--today { left: 818px; }

  .road-photo {
    position: absolute;
    inset: 0;
  }
  .poster--best .road-photo {
    background:
      linear-gradient(180deg,
        var(--dusk) 0%,
        #2a2116 14%,
        var(--olive) 22%,
        var(--amber) 30%,
        #3b2a18 36%,
        #e8e8e8 37.5%,
        var(--road-light) 39%,
        var(--road-mid) 60%,
        var(--road-dark) 100%);
  }
  .poster--invest .road-photo {
    background:
      linear-gradient(180deg,
        var(--sky-blue) 0%,
        #5f6fc8 12%,
        var(--haze) 24%,
        #b57a4a 32%,
        var(--rust) 40%,
        var(--amber) 50%,
        var(--road-light) 56%,
        var(--road-mid) 75%,
        var(--road-dark) 100%);
  }
  .poster--today .road-photo {
    background:
      linear-gradient(165deg,
        var(--haze) 0%,
        #ffffff 30%,
        #5d6ab8 42%,
        var(--rust) 52%,
        var(--amber) 62%,
        var(--olive) 70%,
        var(--road-light) 74%,
        var(--road-mid) 86%,
        var(--road-dark) 100%);
  }

  .label {
    position: absolute;
    display: inline-block;
    background: var(--label-bg);
    color: var(--label-text);
    font-weight: 400;
    white-space: nowrap;
    line-height: 1;
    padding: 5px 8px 6px;
  }
  .label b { font-weight: 700; }

  /* Poster 1 */
  .best-line1 { left: 16px; top: 194px; font-size: 24px; }
  .best-line2 { left: 16px; top: 228px; font-size: 24px; }
  .best-line3 { left: 16px; top: 271px; font-size: 30px; padding: 8px 8px 9px; }

  /* Poster 2 */
  .invest-line1 { left: 21px; top: 326px; font-size: 34px; padding: 8px 9px 9px; }
  .invest-line2 { left: 17px; top: 402px; font-size: 27px; padding: 6px 9px 7px; }

  /* Poster 3 */
  .today-line1 { left: 44px; top: 34px; font-size: 22px; padding: 5px 9px 6px; }
  .today-line2 { left: 15px; top: 76px; font-size: 23px; }
  .today-line3 { left: 15px; top: 111px; font-size: 23px; }
  .today-line4 { left: 15px; top: 144px; font-size: 23px; }
</style>
</head>
<body>
  <main class="series">
    <section class="poster poster--best">
      <div class="road-photo" role="img" aria-label="Motion-blurred highway at dusk with autumn trees along the roadside"></div>
      <span class="label best-line1">If You <b>Want</b> the <b>Best Out</b></span>
      <span class="label best-line2">Of <b>Each Student</b></span>
      <span class="label best-line3"><b>Give</b> the <b>Best Of You!</b></span>
    </section>

    <section class="poster poster--invest">
      <div class="road-photo" role="img" aria-label="Motion-blurred highway under a blue sky with red and orange foliage"></div>
      <span class="label invest-line1"><b>Invest</b> in <b>People</b></span>
      <span class="label invest-line2"><b>Change Someone’s Life</b></span>
    </section>

    <section class="poster poster--today">
      <div class="road-photo" role="img" aria-label="Motion-blurred road curving past colourful autumn landscape"></div>
      <span class="label today-line1">Today Is...</span>
      <span class="label today-line2"><b>Just Another Day</b> for you</span>
      <span class="label today-line3">The <b>MOST IMPORTANT DAY</b></span>
      <span class="label today-line4">in <b>THEIR LIFE</b></span>
    </section>
  </main>
</body>
</html>
```